A private security company called "Tavrin Security Services Ltd"

Hello everybody,

We need a web page for a company based in NZ. It is mainly an informative website so it would be wonderful if the designer puts their absolute best into making it a website that I would really appreciate. The website needs to show professionalism and also needs to make our web surfers find the information they need in a click. the company's colour is black and silver, and if those two colours could be integrated into the website it would be absolutely lovely. Please do contact me for any information.

Sincerely,
Dorian Velasko

Industry/Entity Type

Security

```html
<!DOCTYPE html>
<html lang="en">
<head>
<meta charset="utf-8">
<title>Tavrin Security Services Ltd</title>
<link href="https://fonts.googleapis.com/css2?family=Open+Sans:wght@300;400;600;700&display=swap" rel="stylesheet">
<style>
:root{
  --ink:#222;
  --dark:#2b2b2b;
  --hero:#3a3a3a;
  --text:#777;
  --muted:#999;
  --silver:#e9e9e9;
  --white:#fff;
  --footer-text:#bbb;
}
*{margin:0;padding:0;box-sizing:border-box}
html,body{width:870px;height:1200px;overflow:hidden}
body{position:relative;background:var(--white);font-family:'Open Sans',Arial,sans-serif;color:var(--ink)}
.abs{position:absolute}
a{color:inherit;text-decoration:none}

.topbar{left:0;top:0;width:870px;height:26px;background:var(--dark);color:#eee;font-size:10px}
.topbar .links{left:80px;top:6px;display:flex;gap:15px}
.topbar .social{right:80px;top:7px;display:flex;gap:14px;font-size:8.5px;align-items:center}
.topbar .social span::before{content:"";display:inline-block;width:7px;height:7px;background:#ddd;margin-right:5px;vertical-align:-1px}

.header{left:0;top:26px;width:870px;height:82px;background:var(--white);box-shadow:0 1px 2px rgba(0,0,0,.1)}
.brand{left:80px;top:14px;display:flex;align-items:center;gap:7px;color:var(--ink);font-weight:700}
.brand .mark{width:16px;height:16px;background:var(--ink)}
.brand .name{font-size:15px;letter-spacing:2px;line-height:1}
.brand .sub{font-size:6.5px;letter-spacing:.6px;line-height:1.4}
.nav{right:79px;top:34px;display:flex;gap:24px;font-size:10.4px;color:#888}
.nav .active{color:var(--ink)}

.hero{left:0;top:108px;width:870px;height:324px;background:radial-gradient(ellipse at 45% 40%,#4a4a4a,#333 75%)}
.hero h1{left:80px;top:84px;color:var(--white);font-size:29px;line-height:33px;font-weight:600}
.hero h1 .light{font-weight:300;display:block}
.hero p{left:80px;top:158px;width:290px;color:#bbb;font-size:9.6px;line-height:14.5px}
.hero .btn{left:80px;top:198px;width:92px;height:27px;background:#222;color:var(--white);font-size:11px;line-height:27px;padding-left:13px;clip-path:polygon(0 0,85% 0,100% 50%,85% 100%,0 100%)}
.hero .frame{left:414px;top:50px;width:377px;height:224px;background:var(--white);padding:5px;box-shadow:0 2px 6px rgba(0,0,0,.4)}
.photo{width:100%;height:100%}
.hero .photo{background:linear-gradient(160deg,#7a8fa8 0%,#c9a77a 50%,#5b4a3a 100%)}

.dots{top:442px;left:419px;display:flex;gap:7px}
.dots i{width:6px;height:6px;border-radius:50%;background:#ddd;display:block}
.dots i.on{background:#aaa}

.card{top:472px;width:216px}
.card .frame{height:102px;padding:6px;background:var(--white);box-shadow:0 0 3px rgba(0,0,0,.25)}
.card h3{margin-top:16px;padding-left:6px;font-size:11px;font-weight:400;color:var(--ink)}
.card p{padding-left:6px;margin-top:3px;font-size:9.4px;line-height:14.3px;color:var(--text)}
.c1{left:88px}.c2{left:328px}.c3{left:567px}
.c1 .photo{background:linear-gradient(90deg,#3b5b93,#9bb3d8 60%,#2f4f86)}
.c2 .photo{background:linear-gradient(180deg,#6f8496,#c8ced3 50%,#8d8f86)}
.c3 .photo{background:linear-gradient(90deg,#8c939a,#d4d6d8 50%,#7b3d74)}

.rule{left:80px;top:677px;width:711px;border-top:1px dotted #ccc}

.section-title{font-size:11px;font-weight:400;color:var(--ink)}
.blog{left:87px;top:703px;width:340px}
.post{position:relative;padding-left:20px;margin-top:14px}
.post svg{position:absolute;left:2px;top:1px}
.post h4{font-size:9px;font-weight:400;color:#555}
.post p{margin-top:4px;font-size:9px;line-height:14.5px;color:var(--muted)}
.quote{left:463px;top:703px;width:330px}
.quote p{margin-top:13px;font-size:9px;line-height:14.5px;color:var(--muted)}
.quote .who{display:inline-block;margin-top:6px;font-size:9px;color:#555;text-decoration:underline}
.qdots{left:752px;top:804px;display:flex;gap:6px}
.qdots i{width:8px;height:8px;border-radius:50%;background:#eee;display:block}
.qdots i.on{background:#ccc}

.about{left:0;top:870px;width:870px;height:100px;background:linear-gradient(180deg,#f7f7f7,#e6e6e6);border-top:1px solid #ddd}
.about h2{left:87px;top:22px;font-size:13px;font-weight:400;color:var(--ink)}
.about p{left:87px;top:44px;width:560px;font-size:9.3px;line-height:14.5px;color:#666}
.about .btn{left:678px;top:35px;width:112px;height:31px;background:#1e1e1e;color:var(--white);font-size:13px;line-height:31px;text-align:center}

.footer{left:0;top:970px;width:870px;height:196px;background:radial-gradient(ellipse at 40% 30%,#474747,#2f2f2f 80%)}
.footer .brand{left:80px;top:22px;color:var(--white)}
.footer .brand .mark{background:var(--white)}
.footer .about-text{left:80px;top:92px;width:280px;font-size:9.5px;line-height:14.5px;color:var(--footer-text)}
.footer h3{font-size:13px;font-weight:400;color:var(--white)}
.mail{left:378px;top:19px}
.mail label{display:block;margin-top:13px;font-size:8px;color:#999}
.mail .field{margin-top:4px;width:168px;height:26px;background:#2a2a2a;border:1px solid #252525}
.mail .sub-btn{margin-top:10px;width:84px;height:23px;background:linear-gradient(#fafafa,#d9d9d9);color:var(--ink);font-size:11.5px;line-height:23px;text-align:center;border:1px solid #bbb}
.connect{left:603px;top:19px;width:200px}
.connect .row{display:flex;gap:20px;font-size:8.5px;color:#999;margin-top:32px}
.connect .row + .row{margin-top:14px}
.connect span::before{content:"";display:inline-block;width:11px;height:11px;margin-right:6px;vertical-align:-2px;background:#888;border-radius:2px}
.connect .rss::before{background:#e8842c}
.connect .tw::before{background:#5ab0df}
.connect .fb::before{background:#3f63a6}
.connect .em::before{background:#eee}

.bottombar{left:0;top:1166px;width:870px;height:34px;background:#262626;color:#999;font-size:9.5px}
.bottombar .copy{left:80px;top:10px}
.bottombar .legal{right:79px;top:10px}
.bottombar .legal b{font-weight:400;margin:0 8px}
</style>
</head>
<body>

<div class="topbar abs">
  <nav class="links abs"><a href="#">Home</a><a href="#">About Us</a><a href="#">Contact Us</a><a href="#">Information</a></nav>
  <div class="social abs"><span>RSS</span><span>Chirpline</span><span>Friendbook</span><span>Email</span></div>
</div>

<header class="header abs">
  <div class="brand abs"><div class="mark"></div><div><div class="name">TAVRIN</div><div class="sub">SECURITY SERVICES LTD</div></div></div>
  <nav class="nav abs"><a class="active" href="#">HOME</a><a href="#">ABOUT US</a><a href="#">SECURITY SYSTEM</a><a href="#">SPECIALIZED SECURITY</a><a href="#">CARRERS</a><a href="#">CONTACT US</a></nav>
</header>

<section class="hero abs">
  <h1 class="abs">Newzealand’s Best<span class="light">Security Company</span></h1>
  <p class="abs">Lorem ipsum dolor sit amet, consectetur adipisicing elit, sed do eiusmod tempor incididunt dolore magna aliqua..</p>
  <a class="btn abs" href="#">Learn More</a>
  <div class="frame abs"><div class="photo" role="img" aria-label="Dome security camera above a street with a family walking at sunset"></div></div>
</section>

<div class="dots abs"><i class="on"></i><i></i><i></i></div>

<article class="card c1 abs"><div class="frame"><div class="photo" role="img" aria-label="Security guard standing in front of a wall of monitors"></div></div><h3>PROPERTY GUARDS</h3><p>Lorem ipsum dolor sit amet, consectetur adip-isicing elit, sed do eiusmod tempor incididunt dolore magna aliqua..</p></article>
<article class="card c2 abs"><div class="frame"><div class="photo" role="img" aria-label="Operator with headset at a control room desk"></div></div><h3>SECURITY CONSULTANCY</h3><p>Lorem ipsum dolor sit amet, consectetur adip-isicing elit, sed do eiusmod tempor incididunt dolore magna aliqua..</p></article>
<article class="card c3 abs"><div class="frame"><div class="photo" role="img" aria-label="Investigator on the phone beside window blinds"></div></div><h3>PRIVATE INVESTAGATION</h3><p>Lorem ipsum dolor sit amet, consectetur adip-isicing elit, sed do eiusmod tempor incididunt dolore magna aliqua..</p></article>

<div class="rule abs"></div>

<section class="blog abs">
  <h2 class="section-title">LATEST FROM THE BLOG</h2>
  <div class="post"><svg width="12" height="11" viewBox="0 0 12 11"><path d="M1 1h10v6H5l-3 3V7H1z" fill="none" stroke="#aaa"/></svg><h4>LOREM IPSUM DOLOR SIT AMET CONSECTETUR ADIPSICING ELIT</h4><p>Lorem ipsum dolor sit amet, consectetur adipisicing elit, sed do eiusmod tempor incididunt dolore magna aliqua..</p></div>
  <div class="post"><svg width="12" height="11" viewBox="0 0 12 11"><path d="M1 1h10v6H5l-3 3V7H1z" fill="none" stroke="#aaa"/></svg><h4>LOREM IPSUM DOLOR SIT AMET CONSECTETUR ADIPSICING ELIT</h4><p>Lorem ipsum dolor sit amet, consectetur adipisicing elit, sed do eiusmod tempor incididunt dolore magna aliqua..</p></div>
</section>

<section class="quote abs">
  <h2 class="section-title">WHAT OUR CLIENT’S SAYS :</h2>
  <p>Lorem ipsum dolor sit amet, consectetur adipisicing elit, sed do eiusmod tempor incididunt ut labore et dolore magna aliqua. Ut enim ad minim veniam, quis nostrud exercitation ullamco laboris nisi ut aliquip ex ea commodo consequat.</p>
  <span class="who">MARLOW TEAGUE</span>
</section>
<div class="qdots abs"><i></i><i></i><i class="on"></i></div>

<section class="about abs">
  <h2 class="abs">TAVRIN SECURITY SERVICES LTD</h2>
  <p class="abs">Lorem ipsum dolor sit amet, consectetur adipisicing elit, sed do eiusmod tempor incididunt ut labore et dolore magna aliqua. Ut enim ad minim veniam, quis nostrud exercitation ullamco laboris nisi ut aliquip ex ea commodo consequat.</p>
  <a class="btn abs" href="#">ABOUT US</a>
</section>

<footer class="footer abs">
  <div class="brand abs"><div class="mark"></div><div><div class="name">TAVRIN</div><div class="sub">SECURITY SERVICES LTD</div></div></div>
  <p class="about-text abs">Lorem ipsum dolor sit amet, consectetur adipisicing elit, sed do eiusmod tempor incididunt dolore magna aliqua..</p>
  <div class="mail abs"><h3>Join our Mailing List</h3><label>Email Address</label><div class="field"></div><div class="sub-btn">Subcribe</div></div>
  <div class="connect abs"><h3>Connect With Us</h3>
    <div class="row"><span class="rss">RSS</span><span class="tw">Chirpline</span><span class="fb">Friendbook</span></div>
    <div class="row"><span class="em">Email</span></div>
  </div>
</footer>

<div class="bottombar abs">
  <div class="copy abs">Copyrights © 2014 Tavrin .com - All Rights Reserved</div>
  <div class="legal abs">Privacy Policy<b>|</b>Terms Of Uses</div>
</div>

</body>
</html>
```